Business Card Design

I design and sell kitchens. I would like the card to have a black background either gloss or matt and a stripe through the middle in deep sky blue, the same blue as the team ridgeway pro cycling team. Written in the blue stripe in white i would like Harbourline kitchens in italics. underneath the stripe, again in white i would like 'the complete design and installation service. On the reverse i would like the following in simple black on white
Owen Tramley
07814 296540
email- owentramley@harbourlinekitchens-example.co.uk
Web- WWW.harbourlinekitchens-example.co.uk

I have added a copy of an initial idea for a logo but it can be changed to suit the brief above

Industry/Entity Type

Business

Contact Information for Business Card

Harbourline Kitchens
The complete design and installation service
Owen Tramley
07814 296540-mob
owentramley@harbourlinekitchen-example.co.uk
WWW.harbourlinekitchens-example.co.uk

```html
<!DOCTYPE html>
<html lang="en">
<head>
<meta charset="utf-8">
<title>Harbourline Kitchens – Business Card</title>
<link href="https://fonts.googleapis.com/css2?family=Quicksand:wght@400;500;700&display=swap" rel="stylesheet">
<style>
  :root {
    --backdrop: #e4e5e7;
    --card-black: #050505;
    --card-white: #ffffff;
    --sky-blue: #1ba3e0;
    --white: #ffffff;
    --ink: #0a0a0a;
  }
  * { box-sizing: border-box; margin: 0; padding: 0; }
  html, body {
    width: 1200px;
    height: 800px;
    overflow: hidden;
    background: var(--backdrop);
    font-family: "Quicksand", sans-serif;
  }
  .canvas {
    position: relative;
    width: 1200px;
    height: 800px;
  }
  .card {
    position: absolute;
    top: 232px;
    width: 520px;
    height: 336px;
    border-radius: 4px;
    box-shadow: 0 10px 26px rgba(0, 0, 0, 0.18);
    overflow: hidden;
  }
  .card--front {
    left: 50px;
    background: var(--card-black);
    color: var(--white);
  }
  .card--back {
    left: 630px;
    background: var(--card-white);
    color: var(--ink);
  }

  /* Front */
  .brand-stripe {
    position: absolute;
    left: 0;
    right: 0;
    top: 104px;
    height: 92px;
    background: var(--sky-blue);
    display: flex;
    align-items: center;
    padding-left: 40px;
    gap: 18px;
  }
  .brand-mark {
    width: 52px;
    height: 52px;
    background: var(--white);
    flex: none;
  }
  .brand-name {
    font-weight: 700;
    font-style: italic;
    font-size: 34px;
    line-height: 1;
    letter-spacing: 0.2px;
    color: var(--white);
    white-space: nowrap;
  }
  .tagline {
    position: absolute;
    left: 110px;
    top: 210px;
    font-weight: 400;
    font-size: 22px;
    line-height: 1.15;
    color: var(--white);
  }

  /* Back */
  .contact-list {
    list-style: none;
    position: absolute;
    left: 52px;
    top: 82px;
    display: flex;
    flex-direction: column;
    gap: 16px;
  }
  .contact-item {
    display: flex;
    align-items: center;
    gap: 12px;
    font-size: 16px;
    font-weight: 500;
    letter-spacing: 0.4px;
    white-space: nowrap;
  }
  .contact-item--name {
    font-weight: 700;
    text-transform: uppercase;
    letter-spacing: 1.6px;
    font-size: 15px;
  }
  .contact-icon {
    width: 24px;
    height: 24px;
    flex: none;
    display: block;
  }
  .contact-icon rect.tile { fill: var(--sky-blue); }
  .contact-icon .glyph { fill: var(--ink); }
  .contact-icon .glyph-cut { fill: var(--sky-blue); }
  .contact-icon .glyph-line { fill: none; stroke: var(--ink); stroke-width: 1.6; }
</style>
</head>
<body>
<main class="canvas">

  <section class="card card--front" aria-label="Card front">
    <div class="brand-stripe">
      <span class="brand-mark" aria-hidden="true"></span>
      <span class="brand-name">Harbourline Kitchens</span>
    </div>
    <p class="tagline">the complete design and<br>installation service</p>
  </section>

  <section class="card card--back" aria-label="Card back">
    <ul class="contact-list">
      <li class="contact-item contact-item--name">
        <svg class="contact-icon" viewBox="0 0 24 24" aria-hidden="true">
          <rect class="tile" width="24" height="24"/>
          <circle class="glyph" cx="12" cy="9" r="4"/>
          <path class="glyph" d="M4 21c0-4.5 3.6-7 8-7s8 2.5 8 7z"/>
        </svg>
        Owen Tramley
      </li>
      <li class="contact-item">
        <svg class="contact-icon" viewBox="0 0 24 24" aria-hidden="true">
          <rect class="tile" width="24" height="24"/>
          <rect class="glyph" x="8" y="3" width="9" height="18" rx="1.5"/>
          <rect class="glyph-cut" x="9.5" y="5.5" width="6" height="8"/>
        </svg>
        07814 296540
      </li>
      <li class="contact-item">
        <svg class="contact-icon" viewBox="0 0 24 24" aria-hidden="true">
          <rect class="tile" width="24" height="24"/>
          <rect class="glyph-line" x="4" y="6.5" width="16" height="11"/>
          <path class="glyph-line" d="M4 6.5l8 6.5 8-6.5"/>
        </svg>
        owentramley@harbourlinekitchens-example.co.uk
      </li>
      <li class="contact-item">
        <svg class="contact-icon" viewBox="0 0 24 24" aria-hidden="true">
          <rect class="tile" width="24" height="24"/>
          <circle class="glyph-line" cx="12" cy="12" r="7.5"/>
          <ellipse class="glyph-line" cx="12" cy="12" rx="3.2" ry="7.5"/>
          <path class="glyph-line" d="M4.5 12h15M6 8h12M6 16h12"/>
        </svg>
        www.harbourlinekitchens-example.co.uk
      </li>
    </ul>
  </section>

</main>
</body>
</html>
```